PennaForms Web Page

This is a simple, one page design. I have attached a mockup in QuillWrite along with the PennaForms and BriskSheets logos.

The layout does not need to be recreated, but the fonts/colors might need improvement.

The firm information at the bottom definitely needs help.

Thanks.

```html
<!DOCTYPE html>
<html lang="en">
<head>
<meta charset="utf-8">
<title>PennaForms – Practice Management Software &amp; Document Assembly</title>
<link href="https://fonts.googleapis.com/css2?family=Montserrat:wght@400;500;600;700&family=Open+Sans:ital,wght@0,400;0,600;0,700;1,400&display=swap" rel="stylesheet">
<style>
:root{
  --navy:#0f3461;
  --tan:#b7a684;
  --ink:#222;
  --muted:#7a7a7a;
  --white:#fff;
  --black:#000;
  --footer-grey:#e9e9e9;
}
*{margin:0;padding:0;box-sizing:border-box}
html,body{width:1200px;height:2848px;overflow:hidden;background:var(--white)}
body{position:relative;font-family:"Open Sans",Arial,sans-serif;color:var(--ink)}
.abs{position:absolute}

/* header */
.site-header{left:0;top:0;width:1200px;height:100px;background:var(--white)}
.brand{left:112px;top:26px;display:flex;align-items:center;gap:12px;font-family:"Montserrat",sans-serif;font-weight:600;font-size:34px;color:var(--navy)}
.brand-mark{width:18px;height:18px;background:var(--navy)}
.main-nav{top:38px;left:660px}
.main-nav a{position:absolute;font-family:"Montserrat",sans-serif;font-weight:600;font-size:15px;color:var(--navy);text-decoration:none;white-space:nowrap}
.main-nav a.active{border-bottom:2px solid var(--tan);padding-bottom:6px}

/* hero */
.hero{left:0;top:100px;width:1200px;height:803px;background:linear-gradient(180deg,#d9d3cb 0%,#bdb0a0 45%,#6e5a46 100%)}
.hero-band{left:0;top:342px;width:1200px;height:313px;background:rgba(255,255,255,.62)}
.hero-title{left:0;top:432px;width:1200px;text-align:center;font-family:"Montserrat",sans-serif;font-weight:700;font-size:29px;color:var(--navy)}
.hero-lead{left:140px;top:500px;width:920px;text-align:center;font-size:16px;line-height:24px;color:var(--navy)}
.hero-scroll{left:0;top:585px;width:1200px;text-align:center;font-family:"Montserrat",sans-serif;font-weight:600;font-size:19px;color:#3a2f24}

/* what we do */
.section-title{left:0;top:990px;width:1200px;text-align:center;font-family:"Montserrat",sans-serif;font-weight:500;font-size:40px;letter-spacing:-1px;color:var(--navy)}
.section-tagline{left:0;top:1040px;width:1200px;text-align:center;font-style:italic;font-size:17px;color:var(--muted)}
.section-rule{left:535px;top:1073px;width:130px;height:1px;background:#ddd}
.feature{width:330px;text-align:center}
.feature-icon{display:block;margin:0 auto}
.feature h3{margin-top:12px;font-family:"Montserrat",sans-serif;font-weight:600;font-size:16px;color:var(--navy)}
.feature p{margin:14px auto 0;width:270px;font-size:12.5px;line-height:18px;color:var(--muted)}
.connector{left:0;top:1405px}

/* banner */
.banner{left:0;top:1696px;width:1200px;height:190px;background:var(--navy)}
.banner p{position:absolute;left:0;top:70px;width:1200px;text-align:center;font-family:"Montserrat",sans-serif;font-size:21px;line-height:30px;color:var(--white)}

/* services */
.services{left:116px;top:1962px;width:500px}
.services h2{font-family:"Montserrat",sans-serif;font-weight:500;font-size:27px;color:var(--navy)}
.services p{margin-top:10px;font-family:Arial,"Open Sans",sans-serif;font-size:13px;line-height:17.5px;color:#111}
.services p+p{margin-top:17px}
.partners{left:116px;top:2204px;width:500px;display:flex;gap:26px;align-items:center;white-space:nowrap}
.partners span{font-family:"Open Sans",sans-serif;font-weight:700;font-size:14px;color:var(--navy)}
.laptop-visual{left:640px;top:1975px;width:528px;height:305px;border-radius:14px 14px 6px 6px;background:linear-gradient(160deg,#3a3a3a 0%,#8a6a4e 45%,#d8d8d8 100%)}

/* contact */
.contact{left:0;top:2367px;width:1200px;height:425px;background:var(--black);color:var(--white)}
.contact h2{position:absolute;left:112px;top:50px;font-family:"Open Sans",sans-serif;font-weight:700;font-size:30px}
.contact .intro{position:absolute;left:112px;top:95px;font-size:14px}
.field{position:absolute;background:var(--white);border-radius:2px;font-size:12px;color:#999;padding:10px 10px}
.submit{position:absolute;left:112px;top:326px;width:137px;height:40px;background:var(--tan);color:var(--white);font-weight:700;font-size:20px;text-align:center;line-height:40px;border-radius:2px}
.contact-line{position:absolute;left:847px;display:flex;align-items:center;gap:14px;font-size:19px}
.social{position:absolute;left:845px;top:2583px;display:flex;gap:8px}
.social span{width:40px;height:40px;border-radius:50%;border:2px solid var(--tan)}
.cards{position:absolute;left:847px;top:2641px;display:flex;gap:5px}
.cards span{width:38px;height:26px;border-radius:3px;background:#d7d7d7}

/* footer */
.copyright{left:0;top:2792px;width:1200px;height:56px;background:var(--footer-grey);text-align:center;line-height:56px;font-size:14px;color:#111}
</style>
</head>
<body>

<header class="abs site-header">
  <div class="abs brand"><span class="brand-mark"></span>PennaForms</div>
  <nav class="abs main-nav">
    <a class="active" style="left:0">Home</a>
    <a style="left:73px">Services</a>
    <a style="left:163px">Contact Info</a>
    <a style="left:279px">Payments</a>
    <a style="left:377px">Sign In</a>
  </nav>
</header>

<section class="abs hero" role="img" aria-label="Photo of a team working at laptops around a table in a bright office"></section>
<div class="abs hero-band"></div>
<h1 class="abs hero-title">Practice Management Software &amp; Document Assembly Specialist</h1>
<p class="abs hero-lead">the process of automating your business, eliminating duplication of effort, reducing time spent on routine tasks, increasing productivity and creating more time for the things that matter.</p>
<p class="abs hero-scroll">Scroll to learn a little more about us</p>

<h2 class="abs section-title">What We Do</h2>
<p class="abs section-tagline">Work smarter, not harder</p>
<div class="abs section-rule"></div>

<div class="abs feature" style="left:71px;top:1119px">
  <svg class="feature-icon" width="112" height="114" viewBox="0 0 112 114">
    <circle cx="56" cy="53" r="53" fill="#0f3461"/>
    <circle cx="56" cy="53" r="27" fill="#fff"/>
    <circle cx="56" cy="40" r="4" fill="#0f3461"/>
    <rect x="52" y="48" width="8" height="21" rx="1" fill="#0f3461"/>
    <circle cx="56" cy="108" r="5" fill="#0f3461" stroke="#fff" stroke-width="2"/>
  </svg>
  <h3>Formatica</h3>
  <p>the process of automating your business, eliminating duplication of effort, reducing time spent on routine tasks, increasing productivity and creating more time for the things that matter.</p>
</div>

<div class="abs feature" style="left:437px;top:1119px">
  <svg class="feature-icon" width="112" height="114" viewBox="0 0 112 114">
    <circle cx="56" cy="53" r="53" fill="#b7a684"/>
    <circle cx="56" cy="53" r="29" fill="none" stroke="#fff" stroke-width="3"/>
    <circle cx="56" cy="39" r="6" fill="#fff"/>
    <circle cx="40" cy="64" r="6" fill="#fff"/>
    <circle cx="72" cy="64" r="6" fill="#fff"/>
    <path d="M56 46v8M56 54L42 58M56 54l14 4" stroke="#fff" stroke-width="2.5" fill="none"/>
    <circle cx="56" cy="108" r="5" fill="#b7a684" stroke="#fff" stroke-width="2"/>
  </svg>
  <h3>Practice Management Software</h3>
  <p>software designed to centralize your entire business in one place: file information, contacts, calendaring, notes, telephone logs, email communications, documents, time and billing and more; everyone in the firm can share the information at the same time, something you can never do with a physical file (if you can find it).</p>
</div>

<div class="abs feature" style="left:806px;top:1119px">
  <svg class="feature-icon" width="112" height="114" viewBox="0 0 112 114">
    <circle cx="56" cy="53" r="53" fill="#0f3461"/>
    <path d="M38 28h30l8 8v42H38z" fill="#fff"/>
    <circle cx="49" cy="41" r="5" fill="#0f3461"/>
    <rect x="58" y="38" width="12" height="3" fill="#0f3461"/>
    <rect x="44" y="52" width="26" height="3" fill="#0f3461"/>
    <rect x="44" y="59" width="26" height="3" fill="#0f3461"/>
    <rect x="44" y="66" width="18" height="3" fill="#0f3461"/>
    <circle cx="56" cy="108" r="5" fill="#0f3461" stroke="#fff" stroke-width="2"/>
  </svg>
  <h3>Document Assembly</h3>
  <p>merging data contained in a practice management software, email program, or other database, with QuillWrite or PageCraft, creating perfect documents in seconds, always using the most current contact and file information and never typing the same information twice.</p>
</div>

<svg class="abs connector" width="1200" height="291" viewBox="0 0 1200 291">
  <g fill="none" stroke="#0f3461" stroke-width="3">
    <path d="M172 20v102q0 12 12 12h402q14 0 14 14"/>
    <path d="M1028 20v102q0 12-12 12H614q-14 0-14 14"/>
    <path d="M600 20v240"/>
  </g>
  <circle cx="172" cy="20" r="11" fill="#0f3461"/>
  <circle cx="600" cy="20" r="11" fill="#0f3461"/>
  <circle cx="1028" cy="20" r="11" fill="#0f3461"/>
  <circle cx="600" cy="278" r="28" fill="#fff"/>
  <circle cx="600" cy="278" r="21" fill="#0f3461"/>
  <path d="M590 273l10 10 10-10" fill="none" stroke="#fff" stroke-width="4" stroke-linecap="round" stroke-linejoin="round"/>
</svg>

<section class="abs banner">
  <p>Swift and seamless document assembly. Create complex documents in seconds.<br>Time saved creating documents equals increased profits.</p>
</section>

<section class="abs services">
  <h2>Services Provided</h2>
  <p>Formatica,Inc. provides software support, automation and training to law firms and legal departments throughout Southern California. The Formatica team brings together individuals with several years of experience working in the computer industry, who have all worked in law firms. We understand the daily routine, the language, the deadlines . . . It is this first-hand expertise that sets Formatica, Inc.apart from the crowd.</p>
  <p>It is the goal of Formatica, Inc. to provide the best automation solution available for your firm at a fair price. Extensive resources have been devoted to developing the full integration of:</p>
</section>
<div class="abs partners">
  <span>Lexora</span><span>DocketLine</span><span>BriskSheets</span><span>Chronofile</span><span>PageCraft</span>
</div>
<div class="abs laptop-visual" role="img" aria-label="Laptop showing hands typing on a keyboard"></div>

<section class="abs contact">
  <h2>Contact</h2>
  <p class="intro">Lorem ipsum dolor sit amet, consectetur adipisicing elit sed do eiusmod tempor.</p>
  <div class="field" style="left:112px;top:140px;width:280px;height:40px">Name</div>
  <div class="field" style="left:410px;top:140px;width:280px;height:40px">E-mail</div>
  <div class="field" style="left:112px;top:189px;width:280px;height:42px">Phone</div>
  <div class="field" style="left:410px;top:189px;width:280px;height:42px">Address</div>
  <div class="field" style="left:112px;top:240px;width:578px;height:69px">Message</div>
  <div class="submit">Submit</div>
  <div class="contact-line" style="top:136px">
    <svg width="18" height="18" viewBox="0 0 24 24"><path d="M6.6 10.8a15 15 0 006.6 6.6l2.2-2.2a1 1 0 011-.25 11.4 11.4 0 003.6.57 1 1 0 011 1V20a1 1 0 01-1 1A17 17 0 013 4a1 1 0 011-1h3.5a1 1 0 011 1c0 1.25.2 2.45.57 3.570a1 1 0 01-.25 1z" fill="#fff"/></svg>
    (800) 555-0142
  </div>
  <div class="contact-line" style="top:177px">
    <svg width="20" height="14" viewBox="0 0 20 14"><rect x="1" y="1" width="18" height="12" fill="none" stroke="#b7a684" stroke-width="1.6"/><path d="M1 1l9 7 9-7" fill="none" stroke="#b7a684" stroke-width="1.6"/></svg>
    info@formatica-mail.com
  </div>
</section>
<div class="social"><span></span><span></span><span></span><span></span><span></span></div>
<div class="cards"><span></span><span></span><span></span><span></span><span></span></div>

<footer class="abs copyright">Copyright © 2006-20014 Formatica, Inc</footer>

</body>
</html>
```